Company Culture, Vision, Mission Posters for office

We are rebranding ourselves and have visuals we utilize in our offices that highlight our Mission, Vision, and Company Culture. These visuals will be utilized in posters in our offices, as 8.5" x 11" one-pagers as as trade show banners. I am including the current design, a word document with the content, and visuals of other marketing collateral we are designing.

Font styles to use
Sans Serif

Requirements
Must have
• Use Nexa Bold for headlines and Ebrima for content font

Our orange is CMYK: 2c, 66m, 87y, 0k
Our blue is CMYK: 84c, 69m, 47y, 39k

Culture version must utilize a pyramid to visualize how each pillar in our culture builds on each other.

```html
<!DOCTYPE html>
<html lang="en">
<head>
<meta charset="utf-8">
<title>Vantora Group — Mission</title>
<link href="https://fonts.googleapis.com/css2?family=Montserrat:wght@600;700&family=Noto+Sans:wght@400&display=swap" rel="stylesheet">
<style>
  :root {
    --brand-orange: #ee7838;
    --brand-navy: #2c3c50;
    --paper: #ffffff;
    --backdrop: #e4e5e7;
    --headline-font: "Montserrat", Arial, sans-serif;
    --body-font: "Noto Sans", "Segoe UI", sans-serif;
  }
  * { margin: 0; padding: 0; box-sizing: border-box; }
  html, body {
    width: 1040px;
    height: 1200px;
    overflow: hidden;
    background: var(--backdrop);
  }
  .poster {
    position: absolute;
    left: 70px;
    top: 18px;
    width: 899px;
    height: 1163px;
    background: var(--paper);
    overflow: hidden;
  }
  .poster-shapes {
    position: absolute;
    inset: 0;
  }
  .brand {
    position: absolute;
    left: 482px;
    top: 21px;
    width: 350px;
    text-align: center;
  }
  .brand-dot {
    display: block;
    width: 74px;
    height: 74px;
    margin: 0 auto 22px;
    border-radius: 50%;
    background: var(--brand-orange);
  }
  .brand-name {
    font-family: var(--headline-font);
    font-weight: 700;
    font-size: 39px;
    line-height: 1;
    letter-spacing: 4px;
    color: var(--brand-navy);
    white-space: nowrap;
  }
  .page-title {
    position: absolute;
    left: 55px;
    top: 200px;
    font-family: var(--headline-font);
    font-weight: 700;
    font-size: 42px;
    line-height: 1;
    color: var(--paper);
    letter-spacing: -0.5px;
  }
  .pillar {
    position: absolute;
    left: 35px;
    width: 780px;
  }
  .pillar-heading {
    display: flex;
    align-items: center;
    gap: 12px;
    font-family: var(--headline-font);
    font-weight: 600;
    font-size: 23px;
    line-height: 36px;
    letter-spacing: -0.6px;
    color: var(--brand-orange);
  }
  .pillar-bullet {
    width: 36px;
    height: 36px;
    border-radius: 50%;
    background: var(--brand-orange);
    flex: none;
  }
  .pillar-text {
    margin: 6px 0 0 51px;
    width: 728px;
    font-family: var(--body-font);
    font-size: 21px;
    line-height: 28.2px;
    color: var(--paper);
  }
  .pillar-customers { top: 312px; }
  .pillar-consultants { top: 537px; }
  .pillar-employees { top: 792px; }
  .site-url {
    position: absolute;
    left: 380px;
    top: 1066px;
    width: 390px;
    text-align: center;
    font-family: var(--headline-font);
    font-weight: 600;
    font-size: 21px;
    line-height: 1;
    letter-spacing: 5px;
    color: var(--paper);
  }
</style>
</head>
<body>
  <main class="poster">
    <svg class="poster-shapes" width="899" height="1163" viewBox="0 0 899 1163" aria-hidden="true">
      <rect class="body-panel" x="0" y="220" width="899" height="856" fill="var(--brand-navy)"/>
      <polygon class="title-underband" points="0,157 280,157 296,177 0,177" fill="var(--brand-navy)"/>
      <polygon class="title-band" points="0,177 452,177 494,220 452,270 0,270" fill="var(--brand-orange)"/>
      <polygon class="footer-band" points="264,1033 899,1033 899,1126 264,1126 222,1076" fill="var(--brand-orange)"/>
    </svg>

    <header class="brand">
      <span class="brand-dot"></span>
      <div class="brand-name">VANTORA GROUP</div>
    </header>

    <h1 class="page-title">MISSION</h1>

    <section class="pillar pillar-customers">
      <h2 class="pillar-heading"><span class="pillar-bullet"></span>TO OUR CUSTOMERS</h2>
      <p class="pillar-text">We consistently provide the highest level of value, service, and respect to our customers. Our proven value is driven by professionals committed to providing a superior product. We will stop at nothing to provide the best level of service with organizations that recognize our value and look to establish long-term partnerships.</p>
    </section>

    <section class="pillar pillar-consultants">
      <h2 class="pillar-heading"><span class="pillar-bullet"></span>TO OUR CONSULTANTS</h2>
      <p class="pillar-text">We fully commit to provide value to consultants. Our goal is to provide every job seeker with marketable opportunities and applicable resources that will guide them in achieving their individual business pursuits. Through honest business practices, respect, and open communication we strive to counsel our partners in achieving career success.</p>
    </section>

    <section class="pillar pillar-employees">
      <h2 class="pillar-heading"><span class="pillar-bullet"></span>TO OUR EMPLOYEES</h2>
      <p class="pillar-text">Employees that reflect our core values are our number one commitment. We have created a working environment that fairly rewards performance, creativity, teamwork, and ownership. It is our collective responsibility to challenge and educate one another to achieve personal and shared success.</p>
    </section>

    <footer class="site-url">WWW.VANTORAGROUP.COM</footer>
  </main>
</body>
</html>
```